Merriwick Law - New Letterhead/Logo

Hello!
THE FIRM NAME IS NOW MERRIWICK LAW. We recently just changed our name and we are in need of a classy letterhead. Attached I have a logo we have included in the past, but we are willing to look at other alternatives as well. I will also attach our current letterhead with our old name, Merriwick Law. We are willing to go without attorney names. Please help! Thanks

```html
<!DOCTYPE html>
<html lang="en">
<head>
<meta charset="utf-8">
<title>Merriwick Law Letterhead</title>
<link rel="stylesheet" href="https://fonts.googleapis.com/css2?family=Source+Sans+3:wght@400;600&display=swap">
<style>
  :root {
    --surround: #737373;
    --paper: #ffffff;
    --navy: #0f4c8a;
    --ink: #1a1a1a;
    --watermark: #e6e8f3;
  }
  html, body {
    margin: 0;
    padding: 0;
    width: 1200px;
    height: 1200px;
    overflow: hidden;
    background: var(--surround);
    font-family: "Source Sans 3", sans-serif;
  }
  .letterhead {
    position: absolute;
    left: 117px;
    top: 0;
    width: 926px;
    height: 1200px;
    background: var(--paper);
  }
  .firm-mark {
    position: absolute;
    left: 44px;
    top: 38px;
    display: flex;
    align-items: center;
    gap: 20px;
  }
  .firm-mark__square {
    width: 100px;
    height: 100px;
    background: var(--navy);
  }
  .firm-mark__name {
    color: var(--navy);
    font-weight: 600;
    font-size: 38px;
    line-height: 1.15;
    letter-spacing: 0.5px;
  }
  .attorneys {
    position: absolute;
    right: 26px;
    top: 54px;
    text-align: right;
    font-size: 17px;
    line-height: 22px;
    color: var(--ink);
  }
  .accent-bar {
    position: absolute;
    right: 0;
    top: 58px;
    width: 12px;
    height: 56px;
    background: var(--navy);
  }
  .header-rule {
    position: absolute;
    left: 0;
    top: 178px;
    width: 100%;
    height: 3px;
    background: var(--navy);
  }
  .watermark {
    position: absolute;
    left: 256px;
    top: 393px;
    width: 414px;
    height: 414px;
    background: var(--watermark);
  }
  .contact {
    position: absolute;
    top: 1106px;
    font-size: 17px;
    line-height: 22px;
    color: var(--ink);
  }
  .contact--phone { left: 17px; }
  .contact--phone span { display: inline-block; width: 56px; }
  .contact--address { right: 10px; text-align: right; }
  .footer-band {
    position: absolute;
    left: 0;
    bottom: 0;
    width: 100%;
    height: 31px;
    background: var(--navy);
    color: #fff;
    font-size: 17px;
    line-height: 31px;
    text-align: center;
  }
</style>
</head>
<body>
  <main class="letterhead">
    <header>
      <div class="firm-mark">
        <div class="firm-mark__square"></div>
        <div class="firm-mark__name">Law Offices of<br>Merriwick Law LLC</div>
      </div>
      <div class="attorneys">
        Daniel R. Merriwick, Esq.<br>
        Owen T. Castellane, Esq.<br>
        Peter L. Vandergast, Esq.
      </div>
      <div class="accent-bar"></div>
      <div class="header-rule"></div>
    </header>

    <div class="watermark" aria-hidden="true"></div>

    <footer>
      <div class="contact contact--phone">
        <span>Phone</span>: (555) 214-3086<br>
        <span>&nbsp;Fax</span>: (555) 214-3091
      </div>
      <div class="contact contact--address">
        2180 Alder Ridge Drive Suite 410<br>
        Brookhaven Park, Colorado 80999
      </div>
      <div class="footer-band">www.merriwicklaw.example</div>
    </footer>
  </main>
</body>
</html>
```